Veltrano Community Development Planning New web site

Design a new web site. I have a budget of $1,500.00.
Attached on PowerPoint is a complete site plan. Home page and linked pages.
10 - 12 pages. All copy and photos will be supplied. (300dpi)
I have shown them the concept which they like.
No data bases required. Home page with animations dissolving.
They former web site has been taken down. They have been in business 30 years in New Jersey
Colors teal blues and greens
There will be a new logo)being designed)
The text in home page copy will give you a detailed story what they are all about.

files have been approved for Veltrano, Inc.   Tomas is the designer

Industry/Entity Type

Community

```html
<!DOCTYPE html>
<html lang="en">
<head>
<meta charset="utf-8">
<title>Veltrano Community Development Planning</title>
<link href="https://fonts.googleapis.com/css2?family=Arimo:wght@400;700&display=swap" rel="stylesheet">
<style>
:root{
  --teal:#06a3ad;
  --lime:#b3d978;
  --amber:#fbb829;
  --ink:#111111;
  --white:#ffffff;
}
*{margin:0;padding:0;box-sizing:border-box}
html,body{width:1200px;height:1142px;overflow:hidden;background:var(--white);font-family:'Arimo',Arial,sans-serif;color:var(--ink)}
.page{position:relative;width:1200px;height:1142px}
.site-header{position:absolute;left:0;top:0;width:1200px;height:63px;background:var(--teal)}
.brand{position:absolute;left:23px;top:17px;font-size:35px;line-height:1;color:var(--white);font-weight:400}
.main-nav{position:absolute;left:264px;top:37px;display:flex;align-items:center;font-size:19.3px;color:var(--white);height:26px}
.main-nav .item{white-space:nowrap}
.main-nav .sep{padding:0 12px}
.main-nav .current{background:var(--lime);height:26px;display:flex;align-items:center;padding:0 8px;margin-right:16px}
.header-rule{position:absolute;left:0;top:63px;width:1200px;height:7px;background:var(--lime)}
.hero{position:absolute;left:0;top:70px;width:1200px;height:369px;background:linear-gradient(160deg,#d8d9d8 0%,#f2f2f1 45%,#e4e4e3 75%,#c9c9c8 100%)}
.hero svg{position:absolute;top:0;left:0}
.hero-band{position:absolute;left:0;top:439px;width:1200px;height:19px;background:var(--lime)}
.tagline{position:absolute;left:85px;top:476px;width:1030px;text-align:center;font-size:18.5px;line-height:23px}
.label{position:absolute;height:38px;background:var(--amber);font-size:23px;display:flex;align-items:center;justify-content:center;box-shadow:0 4px 3px -2px rgba(0,0,0,.55)}
.label-about{left:86px;top:560px;width:154px}
.label-results{left:691px;top:561px;width:199px}
.label-members{left:501px;top:885px;width:198px}
.col{position:absolute;top:623px;font-size:13.2px;line-height:16.8px}
.col-about{left:85px;width:527px}
.col-about p{margin-bottom:16.8px}
.col-results{left:690px;width:425px}
.contact-note{position:absolute;left:720px;top:821px;width:450px;font-size:13.4px;line-height:17px;font-weight:700}
.memberships{position:absolute;left:150px;top:946px;width:900px;text-align:center;font-size:17.5px;line-height:21px}
.footer-band{position:absolute;left:0;top:1073px;width:1200px;height:21px;background:var(--amber)}
.site-footer{position:absolute;left:0;top:1112px;width:1200px;text-align:center;font-size:13.4px;color:#222}
</style>
</head>
<body>
<div class="page">
  <header class="site-header">
    <div class="brand">Veltrano</div>
    <nav class="main-nav">
      <span class="item current">Home</span>
      <span class="item">Our Company</span><span class="sep">|</span>
      <span class="item">Services</span><span class="sep">|</span>
      <span class="item">Housing Rehab Application</span><span class="sep">|</span>
      <span class="item">Affordable Application</span><span class="sep">|</span>
      <span class="item">Contact Us</span>
    </nav>
  </header>
  <div class="header-rule"></div>

  <section class="hero" role="img" aria-label="Slideshow photo of rolled architectural blueprints with a pencil and ruler">
    <svg width="1200" height="369" viewBox="0 0 1200 369">
      <polyline points="85,118 40,165 85,212" fill="none" stroke="rgba(255,255,255,.8)" stroke-width="16"/>
      <polyline points="1115,118 1160,165 1115,212" fill="none" stroke="rgba(255,255,255,.8)" stroke-width="16"/>
    </svg>
  </section>
  <div class="hero-band"></div>

  <p class="tagline">Community Development Planning * Housing Rehabilitation Administration * US Department of Housing and Urban Development (HUD) Program Management * Implementation of Programs under the Jurisdiction of New Jersey Council of Affordable Housing (COAH)</p>

  <div class="label label-about">About</div>
  <div class="label label-results">We Get Results</div>

  <div class="col col-about">
    <p>Veltrano, Inc. is a city planning firm that specializes in community development and housing rehabilitation program planning, design and implementation. We have over twenty years of experience in developing and administering income base-base housing and programs in accordance with US Department of Housing and Urban Development (HUD) and New Jersey Council on Affordable Housing (COAH) rules and regulations,</p>
    <p>In addition, our firm is capable of providing the technical and administrative assistance our clients require for implementation of their income based housing programs. E. Martin Dorsey Associates is one of the most experience urban planning firms in New Jersey, with over forty years of as consulting planners.</p>
    <p>To find out more about federal housing programs that we will administer, please go to www.fedhousinginfo.org</p>
  </div>

  <div class="col col-results">
    Veltrano designs income based programs to be supported by federal placement lotteries state funding.<br>
    We implement local programs to benefit people seeking access to affordable housing.<br>
    Our experienced staff screen applicants for local affordable housing.<br>
    We pre-qualify persons who have applied for housing rehabilitation.<br>
    <u>Conduct placement lotteries</u><br>
    Through local housing rehabilitation programs, our experience construction inspectors determine what improvements are required at eligible units based on local building codes and health and safety issues.
  </div>
  <p class="contact-note">For more information about out services, please contact us today at VELTRANO (555) 214-7750 or veltrano@ mailpost.com</p>

  <div class="label label-members">Memberships</div>
  <p class="memberships">National Community Renewal Association &nbsp;&nbsp; New Jersey Regional Planning Association<br>New Jersey Planning Board Officials New Jersey Neighborhood Development Association</p>

  <div class="footer-band"></div>
  <footer class="site-footer">Copy Right 2014 Veltrano, 218 Harbor Crest Road, Lakeview, New Jersey, 08799 &nbsp; TEL (555) 214-7750 Fax (555) 920-3318</footer>
</div>
</body>
</html>
```